website design for B&T Electric

A portfolio website for a high end commercial and residential electrical contracting company. The current site bandtelectric.example does not represent the current direction but the images in the gallery give you an idea of the work we do. Current logo will be uploaded shortly but is black text on white background.
Target Market(s)
General Contractors, Residential Home Owners, clients intersted in Quavis home automation.
Industry/Entity Type
Electrician
Coding
Coded - Design and coding required
Number of Pages Required
2 page
Font styles to use
Sans Serif
Colors
Designer to choose colors to be used in the design.
Requirements
Must have
- Portfolio section highlighting different service areas and products (Quavis Dwellsync, etc)

```html
<!DOCTYPE html>
<html lang="en">
<head>
<meta charset="utf-8">
<title>B&amp;T Electric</title>
<link href="https://fonts.googleapis.com/css2?family=Gelasio:wght@400;700&family=Lato:wght@400;700&display=swap" rel="stylesheet">
<style>
:root{
  --ink:#111418;
  --text:#555a60;
  --blue:#3a6ea8;
  --blue-light:#c9dbee;
  --bar:#1b1d20;
  --footer:#0c0d0f;
  --copy:#3c3e42;
  --white:#ffffff;
  --rule:#c8c8c8;
}
*{margin:0;padding:0;box-sizing:border-box}
html,body{width:1200px;height:2862px;overflow:hidden}
body{font-family:'Lato',sans-serif;color:var(--text);background:var(--white);position:relative}
.abs{position:absolute}

/* header */
.site-header{position:absolute;left:0;top:0;width:1200px;height:97px;background:linear-gradient(#fff,#f1f2f4)}
.logo{left:82px;top:30px;font-family:'Lato',sans-serif;font-weight:700;font-size:32px;color:var(--ink)}
.contact-chip{top:26px;display:flex;align-items:center;gap:16px}
.diamond{width:30px;height:30px;background:var(--ink);transform:rotate(45deg);border-radius:5px;display:flex;align-items:center;justify-content:center}
.diamond svg{transform:rotate(-45deg)}
.chip-label{font-family:'Gelasio',Georgia,serif;font-size:13px;color:var(--blue);line-height:16px}
.chip-value{font-size:15px;color:var(--ink);line-height:20px}

.main-nav{position:absolute;left:0;top:97px;width:1200px;height:44px;background:var(--bar)}
.nav-item{position:absolute;top:0;height:44px;line-height:46px;font-size:13px;color:#b8bcc2;text-transform:uppercase;text-align:center}
.nav-item.active{background:var(--blue);color:#fff;font-weight:700}
.nav-sep{position:absolute;top:16px;width:1px;height:14px;background:#555}
.search{position:absolute;left:906px;top:101px;width:212px;height:35px;border-radius:18px;background:var(--blue-light);font-size:13px;color:#6c7f94;padding:10px 20px}

/* hero */
.hero{left:0;top:141px;width:1200px;height:429px;background:linear-gradient(180deg,#aeb8c2 0%,#c7c9c7 30%,#a39987 60%,#5b4a36 100%)}
.hero-arrow{top:328px;width:34px;height:34px;background:#1e1f21;display:flex;align-items:center;justify-content:center}
.hero-caption{left:0;top:481px;width:1200px;height:89px;background:rgba(20,20,24,.62)}
.hero-welcome{left:0;top:481px;width:391px;height:89px;background:rgba(10,10,12,.55);padding:14px 0 0 82px;font-family:'Gelasio',Georgia,serif;font-size:25px;line-height:31px;color:#fff}
.hero-welcome span{color:#6f9fd6}
.hero-tag{left:440px;top:502px;width:660px;font-size:16px;line-height:24px;color:#e6e6e6}

/* sections */
.section-title{position:absolute;left:0;width:1200px;text-align:center;font-family:'Gelasio',Georgia,serif;font-size:31px;font-weight:400;color:var(--ink)}
.divider{position:absolute;left:382px;width:436px;height:1px;background:var(--rule)}
.divider::after{content:"";position:absolute;left:208px;top:-1px;width:20px;height:3px;background:#888}
.lede{left:100px;top:692px;width:1000px;text-align:center;font-size:13px;line-height:24px;color:#222;font-weight:700}

.service{position:absolute;top:772px;width:260px;text-align:center}
.service-icon{width:108px;height:108px;margin:0 auto;border-radius:50%;background:#f3f3f3;border:1px solid #ddd;display:flex;align-items:center;justify-content:center}
.service-name{margin-top:26px;font-size:13px;font-weight:700;color:var(--ink)}
.service-desc{margin-top:12px;font-size:13px;line-height:24px;color:#666}
.btn-small{display:inline-block;margin-top:12px;width:84px;height:26px;line-height:26px;font-size:11px;color:#fff;background:var(--ink)}
.btn-small.blue{background:var(--blue)}

.about{left:0;top:1070px;width:1200px;height:396px;background:linear-gradient(120deg,#1c2430 0%,#0e1218 55%,#161a20 100%)}
.about-head{position:absolute;top:1118px;font-family:'Gelasio',Georgia,serif;font-size:31px;font-weight:400;color:#fff}
.about-rule{position:absolute;top:1170px;height:1px;background:#3c4450}
.about-text{left:80px;top:1186px;width:636px;font-size:13px;line-height:28.5px;color:#c8ccd2}
.about-text b{color:#fff}
.btn-blue{left:80px;top:1377px;width:132px;height:32px;line-height:32px;text-align:center;font-size:14px;color:#fff;background:var(--blue);border:1px solid #6f9fd6}
.video{left:738px;top:1190px;width:382px;height:218px;background:linear-gradient(180deg,#8fb0d2 0%,#a08a6e 55%,#5b4c3a 100%)}
.video-controls{left:738px;top:1378px;width:382px;height:30px;background:rgba(0,0,0,.75);font-size:12px;color:#fff}

.why-item{position:absolute;width:440px}
.why-icon{position:absolute;left:0;top:0;width:80px;height:80px;border-radius:50%;border:3px solid var(--ink);background:#e9e9e9;display:flex;align-items:center;justify-content:center}
.why-item h3{position:absolute;left:105px;top:10px;font-family:'Gelasio',Georgia,serif;font-size:18px;font-weight:400;color:var(--ink)}
.why-item p{position:absolute;left:105px;top:42px;width:340px;font-size:12.5px;line-height:22px;color:#666}
.why-sep{left:601px;top:1620px;width:1px;height:150px;background:#ddd}

.gallery{left:0;top:1848px;width:1200px;height:632px;background:linear-gradient(180deg,#2a3552 0%,#3a4256 50%,#5a5048 100%)}
.tile{position:absolute;overflow:hidden}
.tile-label{position:absolute;left:0;bottom:0;width:100%;height:41px;line-height:41px;text-align:center;font-family:'Gelasio',Georgia,serif;font-size:18px;color:#fff;background:rgba(0,0,0,.55)}
.tile-feature{background:rgba(0,0,0,.62);text-align:center;color:#fff}
.gal-arrow{top:2190px;font-size:60px;color:rgba(255,255,255,.8);font-weight:300}

.site-footer{left:0;top:2480px;width:1200px;height:336px;background:var(--footer)}
.foot-head{position:absolute;top:2543px;font-family:'Gelasio',Georgia,serif;font-size:21px;color:#fff;letter-spacing:.5px}
.foot-rule{position:absolute;top:2588px;width:164px;height:1px;background:#444}
.foot-vsep{position:absolute;top:2600px;width:1px;height:170px;background:#2c2c2c}
.foot-links{left:80px;top:2604px;list-style:none;font-size:13px;line-height:36.5px;color:#b0b0b0}
.foot-links li::before{content:"› ";color:#888}
.contact-row{position:absolute;left:391px;display:flex;gap:14px;font-size:12.5px;line-height:18px;color:#b0b0b0}
.contact-row svg{flex:none;margin-top:2px}
.field{position:absolute;left:772px;width:348px;background:#fff;font-size:11px;color:#666;padding:7px 8px}
.btn-submit{left:772px;top:2742px;width:161px;height:29px;line-height:30px;text-align:center;font-size:14px;font-weight:700;color:#fff;background:var(--blue)}
.copyright{left:0;top:2816px;width:1200px;height:46px;background:var(--copy);font-size:12px;color:#c8c8c8;padding:15px 82px}
.social{top:2824px;width:30px;height:30px;border-radius:50%;background:#fff}
</style>
</head>
<body>

<header class="site-header">
  <div class="abs logo">B&amp;T Electric</div>
  <div class="abs contact-chip" style="left:653px">
    <div class="diamond"><svg width="14" height="14" viewBox="0 0 24 24"><path fill="#fff" d="M6.6 10.8a15 15 0 006.6 6.6l2.2-2.2a1 1 0 011-.25 11 11 0 003.6.6 1 1 0 011 1V20a1 1 0 01-1 1A17 17 0 013 4a1 1 0 011-1h3.5a1 1 0 011 1 11 11 0 00.6 3.6 1 1 0 01-.25 1z"/></svg></div>
    <div><div class="chip-label">Call Us</div><div class="chip-value">(208) 555-0142</div></div>
  </div>
  <div class="abs contact-chip" style="left:865px">
    <div class="diamond"><svg width="14" height="14" viewBox="0 0 24 24"><path fill="#fff" d="M2 6h20v12H2z"/><path fill="none" stroke="#111418" stroke-width="2" d="M2 6l10 7 10-7"/></svg></div>
    <div><div class="chip-label">Email Us</div><div class="chip-value">dmarsh@bandtelectric.example</div></div>
  </div>
</header>

<nav class="main-nav">
  <div class="nav-item active" style="left:80px;width:96px">Home</div>
  <div class="nav-item" style="left:210px;width:112px">Gallery</div>
  <div class="nav-sep" style="left:340px"></div>
  <div class="nav-item" style="left:360px;width:190px">Speciality Services</div>
  <div class="nav-sep" style="left:568px"></div>
  <div class="nav-item" style="left:590px;width:100px">About</div>
  <div class="nav-sep" style="left:708px"></div>
  <div class="nav-item" style="left:730px;width:130px">Contact Us</div>
</nav>
<div class="search">Search
  <svg class="abs" style="right:16px;top:10px" width="15" height="15" viewBox="0 0 24 24"><circle cx="10" cy="10" r="7" fill="none" stroke="#2d5b8f" stroke-width="3"/><path d="M15 15l6 6" stroke="#2d5b8f" stroke-width="3"/></svg>
</div>

<section>
  <div class="abs hero" role="img" aria-label="Photo of a luxury Mediterranean style home at dusk with lit covered patio"></div>
  <div class="abs hero-arrow" style="left:6px"><svg width="12" height="12" viewBox="0 0 10 10"><path d="M7 1L3 5l4 4" fill="none" stroke="#fff" stroke-width="2"/></svg></div>
  <div class="abs hero-arrow" style="left:1160px"><svg width="12" height="12" viewBox="0 0 10 10"><path d="M3 1l4 4-4 4" fill="none" stroke="#fff" stroke-width="2"/></svg></div>
  <div class="abs hero-caption"></div>
  <div class="abs hero-welcome">Welcom to<br><span>B&amp;T Electric</span></div>
  <div class="abs hero-tag">We expert in Residential Cinemas Make your Home Safe &amp; Secure With our largest audio video control system</div>
</section>

<section>
  <h2 class="section-title" style="top:612px">Our Specialty Services</h2>
  <div class="divider" style="top:668px"></div>
  <p class="abs lede">Lorem ipsum dolor sit amet, consectetuer adipiscing elit, sed diam nonummy nibh euismod tincidunt ut laoreet dolore magna aliquam erat volutpat. Ut wisi enim ad minim veniam, quis nostrud exerci tation Lorem ipsum dolor sit amet, consectetuer adipiscing elit, sed diam</p>

  <div class="service" style="left:61px">
    <div class="service-icon"><svg width="50" height="50" viewBox="0 0 50 50" fill="none" stroke="#111" stroke-width="3"><path d="M4 10l4 4 7-8M4 24l4 4 7-8M4 38l4 4 7-8"/><path d="M22 12h24M22 26h24M22 40h24" stroke="#888"/></svg></div>
    <div class="service-name">Quavis Dwellsync</div>
    <div class="service-desc">We're proudly certified to install<br>Quavis Dwellsync systems.</div>
    <div class="btn-small blue">Read More</div>
  </div>
  <div class="service" style="left:333px">
    <div class="service-icon"><svg width="50" height="50" viewBox="0 0 50 50" fill="none" stroke="#111" stroke-width="2.5"><path d="M6 6h38v34H6zM10 12h30M10 17h30M10 22h30M10 27h30M10 32h30"/><path d="M40 34v10"/></svg></div>
    <div class="service-name">Quavis Lumaglide Motorized Shades</div>
    <div class="service-desc">Quavis Motorized Shades allow you<br>to automatically adjust the natural</div>
    <div class="btn-small">Read More</div>
  </div>
  <div class="service" style="left:605px">
    <div class="service-icon"><svg width="40" height="50" viewBox="0 0 40 50"><path d="M20 3a15 15 0 00-9 27v6h18v-6A15 15 0 0020 3z" fill="#111"/><rect x="12" y="39" width="16" height="4" fill="#111"/><rect x="14" y="45" width="12" height="3" fill="#111"/></svg></div>
    <div class="service-name">LED Lighting</div>
    <div class="service-desc">LED Lighting has rapidly become a<br>functional and affordable option.</div>
    <div class="btn-small">Read More</div>
  </div>
  <div class="service" style="left:877px">
    <div class="service-icon"><svg width="46" height="46" viewBox="0 0 46 46"><rect x="3" y="5" width="40" height="32" rx="3" fill="#111"/><rect x="16" y="11" width="14" height="20" fill="#fff"/><path d="M24 13l-5 9h4l-2 7 6-10h-4z" fill="#111"/><rect x="7" y="37" width="6" height="5" fill="#111"/><rect x="33" y="37" width="6" height="5" fill="#111"/></svg></div>
    <div class="service-name">Emergency Generators</div>
    <div class="service-desc">Never be without power<br>again–protect yourself from frozen</div>
    <div class="btn-small">Read More</div>
  </div>
</section>

<section>
  <div class="abs about" role="img" aria-label="Dimmed photo of a large stone house at night"></div>
  <h2 class="about-head" style="left:80px">About B &amp; T Electric</h2>
  <div class="about-rule" style="left:80px;width:636px"></div>
  <p class="abs about-text"><b>Lorem ipsum dolor sit amet, consectetuer adipiscing elit, sed diam nonummy nibh euismod tincidunt ut laoreet dolore magna aliquam erat volutpat. Ut wisienim ad minim veniam, quis nostrud exerci</b><br>B &amp; T Electric is a full service electrical contracting shop. We offer commercial, residential, light industrial, and agricultural services. We're Quavis Dwellsync and Quavis Motorized Shades certified, as well as an authorized Halvren generator dealer. We've served the Alder Valley and Upper Basin area for over 18 years.</p>
  <div class="abs btn-blue">Read More</div>

  <h2 class="about-head" style="left:738px">Watch Video</h2>
  <div class="about-rule" style="left:738px;width:382px"></div>
  <div class="abs video" role="img" aria-label="Video still of a stone and stucco estate home"></div>
  <div class="abs" style="left:897px;top:1262px;width:64px;height:64px;border-radius:50%;background:rgba(0,0,0,.55)"></div>
  <svg class="abs" style="left:919px;top:1280px" width="24" height="28" viewBox="0 0 24 28"><path d="M2 2l20 12L2 26z" fill="#fff"/></svg>
  <div class="abs video-controls">
    <svg class="abs" style="left:14px;top:9px" width="11" height="12" viewBox="0 0 11 12"><path d="M0 0l11 6-11 6z" fill="#fff"/></svg>
    <span class="abs" style="left:44px;top:8px">04:59</span>
    <div class="abs" style="left:88px;top:13px;width:180px;height:5px;background:#555"></div>
    <div class="abs" style="left:88px;top:13px;width:108px;height:5px;background:#d92b2b"></div>
    <div class="abs" style="left:192px;top:10px;width:11px;height:11px;border-radius:50%;background:#fff"></div>
    <span class="abs" style="left:282px;top:8px">10:35</span>
    <svg class="abs" style="left:322px;top:8px" width="16" height="14" viewBox="0 0 16 14"><path d="M0 4h4l5-4v14l-5-4H0z" fill="#fff"/><path d="M11 3a5 5 0 010 8" stroke="#fff" fill="none" stroke-width="1.5"/></svg>
    <svg class="abs" style="left:352px;top:8px" width="14" height="14" viewBox="0 0 14 14" stroke="#fff" stroke-width="2"><path d="M1 1l12 12M1 5V1h4M13 9v4H9"/></svg>
  </div>
</section>

<section>
  <h2 class="section-title" style="top:1510px">Why Choose Us</h2>
  <div class="divider" style="top:1570px"></div>

  <div class="why-item" style="left:80px;top:1618px">
    <div class="why-icon"><svg width="34" height="40" viewBox="0 0 40 50"><path d="M20 3a15 15 0 00-9 27v6h18v-6A15 15 0 0020 3z" fill="#111"/><rect x="12" y="39" width="16" height="4" fill="#111"/></svg></div>
    <h3>Energy Efficiency</h3>
    <p>Lorem ipsum dolor sit amet, consectetur adipiscing elit. Aenean ac est vitae ipsum tincidunt bibendum.</p>
  </div>
  <div class="why-item" style="left:80px;top:1710px">
    <div class="why-icon"><svg width="34" height="40" viewBox="0 0 34 40" fill="none" stroke="#111" stroke-width="3"><path d="M10 4h14M10 10h14M10 16h14M10 22h14"/><path d="M12 26h10v6h-10zM15 32v5h4v-5" fill="#111"/></svg></div>
    <h3>Innovative Design</h3>
    <p>Lorem ipsum dolor sit amet, consectetur adipiscing elit. Aenean ac est vitae ipsum tincidunt bibendum.</p>
  </div>
  <div class="abs why-sep"></div>
  <div class="why-item" style="left:653px;top:1618px">
    <div class="why-icon"><svg width="38" height="38" viewBox="0 0 38 38"><path d="M4 17h7v17H4z" fill="#111"/><path d="M14 17l7-13c3 0 4 2 3 5l-1 5h9c2 0 3 2 2 4l-4 13c-1 2-2 3-4 3H14z" fill="#111"/></svg></div>
    <h3>Guaranteed Work</h3>
    <p>Lorem ipsum dolor sit amet, consectetur adipiscing elit. Aenean ac est vitae ipsum tincidunt bibendum.</p>
  </div>
  <div class="why-item" style="left:653px;top:1710px">
    <div class="why-icon"><svg width="38" height="38" viewBox="0 0 38 38"><path d="M19 3a8 8 0 00-5 14v3h10v-3a8 8 0 00-5-14z" fill="#111"/><path d="M3 20c3 0 5 4 8 8l4 2v6H9l-6-8zM35 20c-3 0-5 4-8 8l-4 2v6h6l6-8z" fill="#111"/></svg></div>
    <h3>Full Service Solution</h3>
    <p>Lorem ipsum dolor sit amet, consectetur adipiscing elit. Aenean ac est vitae ipsum tincidunt bibendum.</p>
  </div>
</section>

<section>
  <div class="abs gallery" role="img" aria-label="Night photo of a city waterfront with lit buildings reflected on water"></div>
  <div class="abs" style="left:0;top:1848px;width:1200px;height:632px">
    <h2 class="section-title" style="top:55px;color:#fff">Our Gallery</h2>
    <div class="divider" style="top:121px;background:#6a7080"></div>
  </div>
  <div class="abs gal-arrow" style="left:10px">‹</div>
  <div class="abs gal-arrow" style="left:1150px">›</div>

  <div class="tile" style="left:80px;top:2032px;width:263px;height:383px;background:linear-gradient(160deg,#6a6f76,#3d3a36)" role="img" aria-label="Electrician working on a commercial panel"></div>
  <div class="tile tile-feature" style="left:80px;top:2032px;width:263px;height:383px">
    <svg class="abs" style="left:100px;top:90px" width="64" height="58" viewBox="0 0 64 58" fill="#fff"><path d="M4 20h20v36H4zM28 4h32v52H28z"/><g fill="#111"><rect x="9" y="26" width="4" height="5"/><rect x="15" y="26" width="4" height="5"/><rect x="9" y="36" width="4" height="5"/><rect x="15" y="36" width="4" height="5"/><rect x="34" y="12" width="5" height="6"/><rect x="43" y="12" width="5" height="6"/><rect x="52" y="12" width="4" height="6"/><rect x="34" y="24" width="5" height="6"/><rect x="43" y="24" width="5" height="6"/><rect x="34" y="36" width="5" height="6"/><rect x="43" y="36" width="5" height="6"/><rect x="40" y="46" width="8" height="10"/></g></svg>
    <div class="abs" style="left:0;top:178px;width:263px;font-family:'Gelasio',Georgia,serif;font-size:21px">Commercial</div>
    <div class="abs" style="left:20px;top:210px;width:223px;font-size:14px;line-height:21px">Duis autem vel eum iriure do hendrerit in vulputate.</div>
    <svg class="abs" style="left:116px;top:262px" width="32" height="32" viewBox="0 0 32 32" fill="none" stroke="#fff" stroke-width="3"><circle cx="13" cy="13" r="10"/><path d="M20 20l9 9M13 8v10M8 13h10"/></svg>
  </div>
  <div class="tile" style="left:351px;top:2032px;width:246px;height:190px;background:linear-gradient(160deg,#b39466,#5a4a38)" role="img" aria-label="Electrician installing a crystal chandelier"><div class="tile-label">Residential</div></div>
  <div class="tile" style="left:605px;top:2032px;width:244px;height:190px;background:linear-gradient(160deg,#d8dadc,#8d9296)" role="img" aria-label="Hand adjusting a wall mounted control keypad"><div class="tile-label">Quavis Dwellsync</div></div>
  <div class="tile" style="left:857px;top:2032px;width:263px;height:383px;background:linear-gradient(170deg,#1a1a12,#4a4426 60%,#23200f)" role="img" aria-label="Garden path lit with warm landscape lights at night"><div class="tile-label">Landscape</div></div>
  <div class="tile" style="left:351px;top:2230px;width:246px;height:185px;background:linear-gradient(160deg,#e8e2d6,#a89a82)" role="img" aria-label="Living room with motorized window shades"><div class="tile-label">Quavis Shades</div></div>
  <div class="tile" style="left:605px;top:2230px;width:244px;height:185px;background:linear-gradient(160deg,#9c7862,#d6d0c0 60%,#7a6a56)" role="img" aria-label="Standby generator installed beside a brick house"><div class="tile-label">Generators</div></div>
</section>

<footer>
  <div class="abs site-footer"></div>
  <div class="foot-head" style="left:80px">Quick Links</div>
  <div class="foot-rule" style="left:80px"></div>
  <div class="foot-vsep" style="left:314px"></div>
  <ul class="abs foot-links"><li>Home</li><li>Gallery</li><li>Specialty Services</li><li>About</li><li>Contact</li></ul>

  <div class="foot-head" style="left:391px">Contact Details</div>
  <div class="foot-rule" style="left:391px"></div>
  <div class="foot-vsep" style="left:694px"></div>
  <div class="contact-row" style="top:2603px"><svg width="12" height="15" viewBox="0 0 12 16"><path d="M6 0a6 6 0 00-6 6c0 4 6 10 6 10s6-6 6-10a6 6 0 00-6-6z" fill="#fff"/><circle cx="6" cy="6" r="2" fill="#0c0d0f"/></svg><div><b style="color:#fff">B&amp;T Electric</b><br>2150 Ridgeline Way<br>PO Box 4410, Alder Springs, ST 00000</div></div>
  <div class="contact-row" style="top:2680px"><svg width="13" height="13" viewBox="0 0 24 24"><path fill="#fff" d="M6.6 10.8a15 15 0 006.6 6.6l2.2-2.2a1 1 0 011-.25 11 11 0 003.6.6 1 1 0 011 1V20a1 1 0 01-1 1A17 17 0 013 4a1 1 0 011-1h3.5a1 1 0 011 1 11 11 0 00.6 3.6 1 1 0 01-.25 1z"/></svg><div>(208) 555-0142</div></div>
  <div class="contact-row" style="top:2715px"><svg width="13" height="11" viewBox="0 0 24 18"><path d="M0 0h24v18H0z" fill="#fff"/><path d="M0 0l12 9 12-9" fill="none" stroke="#0c0d0f" stroke-width="2"/></svg><div>dmarsh@bandtelectric.example</div></div>
  <div class="contact-row" style="top:2749px"><svg width="13" height="11" viewBox="0 0 24 18"><path d="M0 0h24v18H0z" fill="#fff"/><path d="M0 0l12 9 12-9" fill="none" stroke="#0c0d0f" stroke-width="2"/></svg><div>kpearson@bandtelectric.example</div></div>

  <div class="foot-head" style="left:772px">Quick Inquiry</div>
  <div class="foot-rule" style="left:772px;width:348px"></div>
  <div class="field" style="top:2608px;height:27px">Name:</div>
  <div class="field" style="top:2645px;height:27px">Phone:</div>
  <div class="field" style="top:2679px;height:53px">Message:</div>
  <div class="abs btn-submit">SUBMIT NOW</div>

  <div class="abs copyright">Copyright © 2017 B&amp;T Electric. All Rights Reserved.</div>
  <div class="abs social" style="left:962px"></div>
  <div class="abs social" style="left:1002px"></div>
  <div class="abs social" style="left:1042px"></div>
  <div class="abs social" style="left:1082px"></div>
</footer>

</body>
</html>
```